Lorvika.no is a new website about pedagogical entrepreneurship. It's main target group is teachers. The Fjellmark Institute for Classroom Media and the Nordvik Agency for Schools and Study are leading the project.

The web page is meant to show examples of how different methods of entrepreneurship can be used pedagogical in a learning environment. The page will also support the user with examples of different teaching programs and other examples of best practice.

Pedagogical entrepreneurship is not about business and men in suits. It's a method for learning. The focus in the design should be on school, education and new ways of learning.

The final product should be motivating and engaging, but at the same time governmental and serious. We are not looking for something "flashy" and corporate-looking, but a moderate, task-focused and clean design that state quality.

We need designs for three pages:
1 - frontpage
2 - subpage ("Metoder og undervisningsopplegg")
3 - subpage ("Smått-VERK i Brekkelia")

The interaction design for these three pages will be uploaded as an attachment.

We would like you to find inspiration in the following websites:
- www.gryvekst.no
- www.lavrek.no
- www.tovandstudio.com
- www.kvp.no
(more will be added)

Please use the attached logo, and feel free to use this as an inspiration for the rest of the design.

Target Market(s)

Teachers

Industry/Entity Type

Education

Requirements
Must have
• * Header with: Logo. Main navigation. Utility navigation. Search box.
* Footer
Should not have
• Images of men in suits.
Very strong graphical elements that stands out too much (we want it clean).

```html
<!DOCTYPE html>
<html lang="en">
<head>
<meta charset="utf-8">
<title>Lorvika.no – Pedagogical Entrepreneurship</title>
<link rel="stylesheet" href="https://fonts.googleapis.com/css2?family=Arimo:wght@400;700&display=swap">
<style>
:root{
  --yellow:#f2b705;
  --yellow-text:#e8ac00;
  --blue:#45a9dc;
  --blue-dark:#2d86c4;
  --navy:#1f3a66;
  --ink:#333333;
  --grey:#7a7a7a;
  --dark:#3a3a3a;
  --nav-dark:#3c3c3c;
  --white:#ffffff;
  --page:#fbfbfb;
}
*{box-sizing:border-box;margin:0;padding:0}
html,body{width:786px;height:1200px;overflow:hidden}
body{position:relative;background:var(--page);font-family:"Arimo",Arial,sans-serif;color:var(--ink)}
.abs{position:absolute}
a{color:inherit;text-decoration:none}
ul{list-style:none}

/* header */
.brand{left:28px;top:22px;display:flex;align-items:center;gap:12px}
.brand-mark{width:40px;height:40px;border-radius:50%;background:var(--blue-dark)}
.brand-name{font-size:34px;font-weight:700;color:var(--blue-dark);letter-spacing:-1px;line-height:1}
.brand-tag{left:96px;top:58px;font-size:7px;color:var(--navy);font-weight:700}
.search{left:601px;top:20px;width:119px;height:18px;border:1px solid #bbb;border-radius:9px;background:#fff;font-size:9px;color:#aaa;padding:3px 0 0 18px}
.search svg{position:absolute;right:7px;top:3px}
.main-nav{left:335px;top:47px;width:385px;height:20px;display:flex}
.main-nav a{display:flex;align-items:center;justify-content:center;gap:6px;font-size:11px;color:#fff;background:var(--nav-dark)}
.main-nav a:nth-child(1){width:140px;background:var(--yellow);color:#222}
.main-nav a:nth-child(2){width:122px}
.main-nav a:nth-child(3){width:123px}
.plus{width:9px;height:9px;border-radius:50%;background:#fff;position:relative;display:inline-block}
.plus::before,.plus::after{content:"";position:absolute;background:var(--nav-dark);left:2px;top:4px;width:5px;height:1px}
.plus::after{left:4px;top:2px;width:1px;height:5px}

/* intro */
.hero-art{left:28px;top:111px;width:194px;height:309px;border-radius:6px;background:linear-gradient(160deg,#c97a3a,#8e4a1c 60%,#5a2e12)}
.hero-title{left:335px;top:113px;font-size:16.5px;font-weight:700;color:var(--ink);letter-spacing:.3px}
.hero-title span{color:var(--yellow-text)}
.hero-text{left:335px;top:153px;width:385px;font-size:10.5px;line-height:13px;color:#888;letter-spacing:.3px}
.btn-more{left:335px;top:187px;width:140px;height:21px;background:linear-gradient(#5cb8ea,#2e8fd0);color:#fff;font-size:11px;display:flex;align-items:center;justify-content:center;gap:30px;padding-left:10px}
.btn-more .plus::before,.btn-more .plus::after{background:var(--blue-dark)}
.feature{top:228px;width:150px;text-align:center}
.feature .tile{width:92px;height:92px;margin:11px auto 0;transform:rotate(45deg);border-radius:14px;background:#fff;border:1px solid #c8c8c8;box-shadow:0 2px 4px rgba(0,0,0,.18)}
.feature .icon{position:absolute;left:50px;top:39px;width:50px;height:50px;border-radius:50%;background:var(--yellow)}
.feature .cap{margin-top:35px;font-size:8.5px;color:#111}
.feature .link{margin-top:7px;font-size:9.5px;line-height:11px;color:var(--blue-dark)}

/* get started band */
.band{left:0;top:0}
.survey-q{left:42px;top:496px;font-size:10.5px;line-height:13px;color:#fff;letter-spacing:.2px}
.gauge{left:37px;top:554px;width:120px;height:78px;background:linear-gradient(135deg,#24406f,#1a2f52);border-radius:60px 60px 8px 8px}
.survey-link{left:44px;top:657px;font-size:10.5px;color:#fff;text-decoration:underline}
.divider{left:238px;top:486px;height:204px;border-left:3px dotted #fff}
.started{left:337px;top:485px;font-size:19px;color:#fff;letter-spacing:.5px;display:flex;align-items:center;gap:3px}
.col-title{font-size:14px;color:var(--ink);letter-spacing:.5px}
.col-list{margin-top:12px;font-size:10.5px;line-height:13px;color:#fff}
.see-more{display:flex;align-items:center;gap:10px;font-size:10.5px;color:#fff}
.dot-plus{width:12px;height:12px;border-radius:50%;background:var(--dark);position:relative}
.dot-plus::before,.dot-plus::after{content:"";position:absolute;background:#fff;left:3px;top:5.5px;width:6px;height:1px}
.dot-plus::after{left:5.5px;top:3px;width:1px;height:6px}

/* carousel */
.rail{left:14px;top:729px;width:14px;height:220px;background:linear-gradient(90deg,#f0f0f0,#d8d8d8)}
.slide{top:738px;width:212px;text-align:center}
.slide h3{font-size:10.5px;font-weight:400;color:var(--navy);letter-spacing:.2px}
.slide .photo{margin-top:8px;height:126px;border-radius:8px;background:linear-gradient(#d8d4cc 0%,#b49a8a 45%,#6c7a5e 70%,#e6eef3 100%);box-shadow:0 1px 3px rgba(0,0,0,.3)}
.arrow{top:823px;width:21px;height:23px;background:var(--yellow);border-radius:3px}
.arrow svg{position:absolute;left:6px;top:6px}

/* footer */
.social{top:938px;display:flex;gap:12px;left:628px}
.social span{width:12px;height:12px;border-radius:50%;background:#9a9a9a}
.foot-brand{left:34px;top:1010px;display:flex;align-items:center;gap:10px}
.foot-brand .sq{width:26px;height:26px;background:#fff;border-radius:4px}
.foot-brand b{font-size:28px;color:#fff;font-weight:700}
.foot-col{font-size:9.5px;line-height:11px;color:#fff}
.foot-col h4{font-size:11px;font-weight:400;color:var(--yellow);margin-bottom:10px}
.foot-more{font-size:7.5px;color:var(--yellow);margin-top:14px}
.copyright{left:29px;top:1158px;font-size:8.5px;color:#ddd}
.legal{left:599px;top:1158px;font-size:8.5px;color:#eee}
</style>
</head>
<body>

<!-- header -->
<div class="abs brand"><span class="brand-mark"></span><span class="brand-name">Lorvika</span></div>
<div class="abs brand-tag">Entreprenørielle metoder i undervisningen</div>
<div class="abs search">Search
  <svg width="10" height="10" viewBox="0 0 10 10"><circle cx="4" cy="4" r="3" fill="none" stroke="#222" stroke-width="1.5"/><line x1="6.2" y1="6.2" x2="9.3" y2="9.3" stroke="#222" stroke-width="1.6"/></svg>
</div>
<nav class="abs main-nav">
  <a href="#">Best Practice Schools <span class="plus"></span></a>
  <a href="#">Lorvikameter <span class="plus"></span></a>
  <a href="#">About Lorvika.no <span class="plus"></span></a>
</nav>

<!-- intro -->
<div class="abs hero-art" role="img" aria-label="Illustration of a wooden pencil holder with pencils, brushes and a photo strip"></div>
<h1 class="abs hero-title"><span>PEDAGOGICAL ENTERPRENEURSHIP</span> WORKS</h1>
<p class="abs hero-text">Duis vitae leo sit amet ligula consectetur adipiscing ac sit amet urna. Nulla malesuada, nisi tristique convallis molestie, felis massa porttitor</p>
<a class="abs btn-more" href="#">Learn More <span class="plus"></span></a>

<div class="abs feature" style="left:324px">
  <div class="tile"></div><div class="icon" role="img" aria-label="Icon of a light bulb over an open book"></div>
  <p class="cap">Learn about what,why &amp; how!</p>
  <p class="link">What is Pedagogical<br>Entrepreneurship</p>
</div>
<div class="abs feature" style="left:473px">
  <div class="tile"></div><div class="icon" role="img" aria-label="Icon of a pencil writing on paper"></div>
  <p class="cap">Plan your Lessons!</p>
  <p class="link">Methods &amp; Teaching Plans</p>
</div>
<div class="abs feature" style="left:620px">
  <div class="tile"></div><div class="icon" role="img" aria-label="Icon of cheering figures"></div>
  <p class="cap">Be Inspired!</p>
  <p class="link">Good Examples / Best Practice</p>
</div>

<!-- get started band -->
<svg class="abs band" width="786" height="1200" viewBox="0 0 786 1200" aria-hidden="true">
  <polygon points="0,459 786,411 786,665 0,729" fill="#45a9dc"/>
  <line x1="0" y1="453" x2="786" y2="405" stroke="#45a9dc" stroke-width="3" stroke-dasharray="3 3"/>
  <line x1="0" y1="465" x2="786" y2="417" stroke="#fff" stroke-width="2.5" stroke-dasharray="3 3"/>
  <polygon points="0,951 786,893 786,1200 0,1200" fill="#3a3a3a"/>
  <line x1="0" y1="945" x2="786" y2="887" stroke="#3a3a3a" stroke-width="3" stroke-dasharray="3 3"/>
  <line x1="0" y1="957" x2="786" y2="899" stroke="#fff" stroke-width="2.5" stroke-dasharray="3 3"/>
</svg>

<p class="abs survey-q">Are You Working<br>Enterpreneurship-like?</p>
<div class="abs gauge" role="img" aria-label="Gauge dial with a needle"></div>
<a class="abs survey-link" href="#">Try the Lorvikameter</a>
<div class="abs divider"></div>

<h2 class="abs started">GET STARTED!
  <svg width="20" height="20" viewBox="0 0 20 20"><path d="M6 5 A7 7 0 1 0 14 5" fill="none" stroke="#fff" stroke-width="2"/><line x1="10" y1="1" x2="10" y2="10" stroke="#fff" stroke-width="2"/></svg>
</h2>

<section class="abs" style="left:337px;top:546px">
  <h3 class="col-title">METHODS</h3>
  <ul class="col-list"><li>Cafe Pedagogikk</li><li>Elevbedrift</li><li>Grundercamp</li><li>Story line</li><li>Real</li></ul>
</section>
<a class="abs see-more" href="#" style="left:337px;top:661px">See more <span class="dot-plus"></span></a>

<section class="abs" style="left:593px;top:544px">
  <h3 class="col-title">TEACHING PLANS</h3>
  <ul class="col-list"><li>Teaching Plan title</li><li>Teaching Plan title</li><li>Teaching Plan title</li><li>Teaching Plan title</li><li>Teaching Plan title</li></ul>
</section>
<a class="abs see-more" href="#" style="left:591px;top:654px">See more <span class="dot-plus"></span></a>

<!-- carousel -->
<div class="abs rail"></div>
<a class="abs arrow" href="#" style="left:20px" aria-label="Previous"><svg width="9" height="11"><polygon points="8,0 8,11 0,5.5" fill="#6b4b00"/></svg></a>
<a class="abs arrow" href="#" style="left:744px" aria-label="Next"><svg width="9" height="11"><polygon points="0,0 0,11 8,5.5" fill="#6b4b00"/></svg></a>
<article class="abs slide" style="left:67px"><h3>Smått-VERK at Brekkelia School</h3><div class="photo" role="img" aria-label="Photo of a school building in winter with pupils and market stalls"></div></article>
<article class="abs slide" style="left:297px"><h3>Smått-VERK at Brekkelia School</h3><div class="photo" role="img" aria-label="Photo of a school building in winter with pupils and market stalls"></div></article>
<article class="abs slide" style="left:521px"><h3>Smått-VERK at Brekkelia School</h3><div class="photo" role="img" aria-label="Photo of a school building in winter with pupils and market stalls"></div></article>

<!-- footer -->
<div class="abs social" aria-label="Social links"><span></span><span></span><span></span><span></span></div>
<div class="abs foot-brand"><span class="sq"></span><b>Lorvika</b></div>

<div class="abs foot-col" style="left:208px;top:1000px">
  <h4>Pedagogical Entrepreneurship</h4>
  <ul><li>What is pedagogical entrepreneuship?</li><li>Science</li><li>Best Practice Schools</li><li>Lorvikameteret</li></ul>
</div>
<div class="abs foot-col" style="left:208px;top:1109px"><h4>About Lorvika.no</h4></div>

<div class="abs foot-col" style="left:466px;top:1000px">
  <h4>Meethods</h4>
  <ul><li>Story line</li><li>Real</li><li>Cafe-pedagogikk</li></ul>
  <p class="foot-more">See More..</p>
</div>
<div class="abs foot-col" style="left:466px;top:1091px">
  <h4>Teaching Plans</h4>
  <ul><li>Title</li><li>Title</li><li>Title</li></ul>
  <p class="foot-more">See More..</p>
</div>
<div class="abs foot-col" style="left:661px;top:1000px">
  <h4>Gode eksempler</h4>
  <ul><li>Smått-VERK at Brekkelia</li><li>Smått-VERK at Brekkelia</li><li>Smått-VERK at Brekkelia</li></ul>
  <p class="foot-more">See More...</p>
</div>

<p class="abs copyright">© 2012 Lorvika.no. All Right Reserved</p>
<p class="abs legal">Terms and Conditions | Privacy Policy</p>

</body>
</html>
```